Re-design existing website and add products for sale.

Our current website is very basic and cluttered. (brightwillowcare.com.au)We want a modern looking website that is easy to navigate. We also want to start selling essential oils and crystal products, so there needs to be a separate page for this. Also needs to be easily edited as we need to change the monthly oracle card with the description. Would like calming colours as we are all about natural healing. Alongside the services listed there should be a button to book now which asks for their name, email, phone number ect. and adds it to the cart.

• Logo is still being designed, please leave a space for the logo which will basically be a lotus flower within a mandala.

```html
<!DOCTYPE html>
<html lang="en">
<head>
<meta charset="utf-8">
<title>Bright Willow Care – Services</title>
<link rel="stylesheet" href="https://fonts.googleapis.com/css2?family=Lexend:wght@500;600&family=Questrial&family=PT+Sans:wght@400;700&family=Cousine&display=swap">
<style>
  :root {
    --teal: #3f9a98;
    --teal-dark: #358886;
    --button: #84d4d6;
    --button-text: #f4ffff;
    --active: #ffffff;
    --active-text: #2f8c8a;
    --accent: #d05e5c;
    --ink: #141414;
    --heading-light: #eef7f4;
    --petal: #f6d7e6;
  }
  * { margin: 0; padding: 0; box-sizing: border-box; }
  html, body { width: 1200px; height: 675px; overflow: hidden; }
  body { position: relative; background: var(--teal); font-family: "PT Sans", sans-serif; color: var(--ink); }

  .site-header {
    position: absolute; left: 0; top: 0; width: 1200px; height: 128px;
    background: linear-gradient(135deg, var(--teal) 0%, var(--teal-dark) 100%);
  }
  .logo-space {
    position: absolute; left: 23px; top: 22px; width: 76px; height: 76px;
    border-radius: 50%; border: 2px dashed var(--heading-light); opacity: 0.8;
  }
  .brand-name {
    position: absolute; left: 112px; top: 20px;
    font-family: "Lexend", sans-serif; font-weight: 600; font-size: 36px;
    color: var(--heading-light); letter-spacing: 0.3px;
  }
  .brand-tagline {
    position: absolute; left: 112px; top: 66px;
    font-family: "Questrial", sans-serif; font-size: 15px; color: var(--heading-light);
  }
  .nav-button {
    position: absolute; top: 27px; width: 89px; height: 41px; border-radius: 8px;
    background: var(--button); color: var(--button-text);
    font-family: "Cousine", monospace; font-size: 12px;
    display: flex; align-items: center; justify-content: center;
  }
  .nav-button.is-active { background: var(--active); color: var(--active-text); }
  .nav-sub {
    position: absolute; left: 746px; top: 79px; width: 89px; height: 35px; border-radius: 7px;
    background: var(--accent); color: #fff; font-family: "Cousine", monospace; font-size: 12px;
    line-height: 14px; text-align: center; display: flex; align-items: center; justify-content: center;
  }

  .services {
    position: absolute; left: 0; top: 129px; width: 1200px; height: 375px;
    background:
      radial-gradient(ellipse 180px 120px at 30% 20%, var(--petal) 0%, transparent 70%),
      radial-gradient(ellipse 220px 160px at 62% 60%, var(--petal) 0%, transparent 70%),
      radial-gradient(ellipse 200px 150px at 92% 15%, #ead3f0 0%, transparent 70%),
      #fdfbfc;
    box-shadow: 0 2px 6px rgba(0,0,0,0.35), 0 -2px 6px rgba(0,0,0,0.35);
  }
  .service-image { position: absolute; }
  .service-title {
    position: absolute; font-family: "Lexend", sans-serif; font-weight: 500; font-size: 16.5px; line-height: 19px;
  }
  .service-price {
    position: absolute; font-family: "Questrial", sans-serif; font-size: 13px; line-height: 14.5px;
  }
  .book-button {
    position: absolute; height: 20px; padding: 0 12px; border-radius: 5px;
    background: var(--accent); color: #fff; font-family: "Cousine", monospace; font-size: 11px;
    display: flex; align-items: center;
  }
  .service-copy {
    position: absolute; font-size: 10px; line-height: 12.6px; letter-spacing: -0.1px;
  }
  .service-copy p { margin-bottom: 6px; }
  .offer-heading {
    position: absolute; left: 833px; top: 215px;
    font-family: "Lexend", sans-serif; font-weight: 500; font-size: 16.5px;
  }

  .contact {
    position: absolute; left: 191px; top: 523px; color: var(--heading-light);
  }
  .contact-title { font-family: "Lexend", sans-serif; font-weight: 600; font-size: 24px; }
  .contact-lead { font-family: "Questrial", sans-serif; font-size: 13.5px; margin: 2px 0 0 2px; }
  .contact-details { margin: 10px 0 0 2px; font-size: 10px; line-height: 14.8px; font-weight: 700; }
</style>
</head>
<body>
  <header class="site-header">
    <div class="logo-space" aria-label="Space reserved for logo"></div>
    <div class="brand-name">Bright Willow Care</div>
    <div class="brand-tagline">“Find Your True Self and Bring Balance to Your Life”</div>
    <nav>
      <div class="nav-button" style="left:518px">Welcome</div>
      <div class="nav-button" style="left:632px">About Me</div>
      <div class="nav-button is-active" style="left:746px">Services</div>
      <div class="nav-button" style="left:860px">Shop</div>
      <div class="nav-button" style="left:974px">Book Now</div>
      <div class="nav-button" style="left:1088px">Contact Me</div>
      <div class="nav-sub">Monthly<br>Oracle Card</div>
    </nav>
  </header>

  <main class="services">
    <svg class="service-image" style="left:23px;top:13px" width="90" height="101" role="img" aria-label="Photo of healing hands with glowing light">
      <defs><radialGradient id="glow"><stop offset="0" stop-color="#fff4e6"/><stop offset="0.6" stop-color="#e8a27e"/><stop offset="1" stop-color="#b5553a"/></radialGradient></defs>
      <rect width="90" height="101" rx="10" fill="url(#glow)"/>
    </svg>
    <div class="service-title" style="left:122px;top:47px">Reiki/Seichim Healings</div>
    <div class="service-price" style="left:122px;top:66px">1 Hour - $75<br>1/2 Hour - $40</div>
    <div class="book-button" style="left:122px;top:98px">Book Now</div>
    <div class="service-copy" style="left:23px;top:128px;width:440px">
      <p><b>Reiki</b> is a non-intrusive, wonderful hands-on healing technique,<br>which can help boost and balance your energy levels,<br>strengthen your immune system, help you relax and<br>let go of stress and tension and help to maintain your overall health<br>and wellbeing. It can help clear blockages and clear past lives and<br>is a great technique for cleansing the body and breaking down stale energy blockages</p>
      <p><b>Seichim</b> is an ancient and sacred healing modality.<br>It is an advanced form of healing which involves the use of sacred geometry symbols<br>using two hands.<br>It helps clear past lives in a different way to Reiki and helps release blockages<br>from your energy field.<br>It is a form of healing which has been taught in many mystery schools in ancient times.<br>Seichim is said to be the parent energy of all hands-on healing systems and is believed to have<br>originated from Atlantean times.<br>It can be shown that Seichim was practiced by the Mayan civilisation in South America<br>before being introduced to Egypt.</p>
    </div>

    <svg class="service-image" style="left:492px;top:16px" width="42" height="99" role="img" aria-label="Brush-lettered Reiki symbol">
      <rect width="42" height="99" fill="#ecebe8"/>
    </svg>
    <div class="service-title" style="left:566px;top:40px">Reiki &amp; Seichim Workshops</div>
    <div class="service-price" style="left:566px;top:58px">Reiki 1 Workshop - $180<br>Reiki 2 Workshop - $280<br>Seichim Workshop - $460</div>
    <div class="book-button" style="left:566px;top:104px">Book Now</div>
    <div class="service-copy" style="left:468px;top:132px;width:360px">
      <p><b>Reiki</b> is Japanese for Universal Life Force Energy.<br><b>Rei</b> = Universal<br><b>Ki</b> = Vital Energy</p>
      <p>Would you like to feel more grounded, self empowered,<br>confident and relaxed?</p>
      <p>Have you had the chance to experience Reiki or Seichim and<br>now wish to further your knowledge of these<br>ancient healing techniques and use them to help yourself and<br>others around you?</p>
      <p>I offer Reiki 1 &amp; 2 workshops as well as Seichim workshops where<br>I work one on one with you to teach you these wonderful techniques.</p>
      <p>Prerequisites:<br>Reiki 1 - None<br>Reiki 2 - Reiki 1 Certificate<br>Isis Seichim - Reiki 1 &amp; 2 Certificates</p>
    </div>

    <svg class="service-image" style="left:833px;top:13px" width="88" height="104" role="img" aria-label="Oracle card deck cover artwork">
      <defs><linearGradient id="deck" x1="0" y1="0" x2="0" y2="1"><stop offset="0" stop-color="#b69ad0"/><stop offset="1" stop-color="#8a76b4"/></linearGradient></defs>
      <rect width="88" height="104" fill="url(#deck)"/>
    </svg>
    <div class="service-title" style="left:929px;top:55px">Oracle Card Readings</div>
    <div class="service-price" style="left:929px;top:73px">20 Min - $30</div>
    <div class="book-button" style="left:929px;top:94px">Book Now</div>
    <div class="service-copy" style="left:833px;top:128px;width:360px">
      <p>Oracle cards, also known as wisdom cards are cards used for divination,<br>fortune telling and spiritual guidance.</p>
      <p>Oracle cards are the modern version of tarot cards,<br>which have been used for centuries by people to find meaningful answers to<br>questions about their life, spiritual path and future.</p>
    </div>
    <div class="offer-heading">Some of the services on offer include:</div>
    <div class="service-copy" style="left:833px;top:236px;width:360px">
      Reiki &amp; Seichim Healings<br>Energy Healing<br>Chakra Balancing<br>Energy Balancing<br>Past Life Clearing<br>Oracle Card Readings/Online Readings<br>Distant Healing<br>Reiki &amp; Seichim Workshops<br>Crystals &amp; Hand Made Jewellery Available<br>Essential Oil Roll On Blends Available
    </div>
  </main>

  <footer class="contact">
    <div class="contact-title">Contact Me</div>
    <div class="contact-lead">Got a question? Feel free to ask.</div>
    <div class="contact-details">Tel: 0400 118 362<br>14 Marrow Lane<br>Kestrel, SA 5099<br>hello@brightwillowcare.com.au</div>
  </footer>
</body>
</html>
```